Vantrell Law Letterhead

We need a new letterhead design for a Law Firm. The address for the law firm is 4817 Larkspur Boulevard, Suite 250, Houston, Texas 77342. Phone Number: 832-619-3057; Fax Number: 832-407-1694. The logo is uploaded to the project.

```html
<!DOCTYPE html>
<html lang="en">
<head>
<meta charset="utf-8">
<title>Vantrell Law Letterhead</title>
<link href="https://fonts.googleapis.com/css2?family=Noto+Serif:wght@400;700&display=swap" rel="stylesheet">
<style>
  :root {
    --backdrop: #c9c9c9;
    --paper: #f4f4f4;
    --navy: #14204f;
    --red: #c8161d;
    --ink: #1a1a1a;
  }
  * { margin: 0; padding: 0; box-sizing: border-box; }
  html, body { width: 1070px; height: 1200px; overflow: hidden; }
  body { background: var(--backdrop); font-family: "Noto Serif", Georgia, serif; color: var(--ink); }
  .letterhead {
    position: absolute; left: 202px; top: 112px;
    width: 660px; height: 941px; background: var(--paper); overflow: hidden;
  }
  .brand {
    position: absolute; left: 43px; top: 64px;
    display: flex; align-items: center; gap: 14px;
  }
  .brand-mark { width: 34px; height: 34px; background: var(--navy); }
  .brand-name { font-size: 36px; font-weight: 400; color: var(--navy); letter-spacing: 0.5px; line-height: 1; }
  .contact {
    position: absolute; right: 37px; top: 40px;
    text-align: right; font-size: 12px; line-height: 13.5px; font-style: normal;
  }
  .contact-rule { width: 140px; height: 2px; background: var(--red); margin: 9px 0 9px auto; }
  .salutation { position: absolute; left: 47px; top: 218px; font-size: 16px; font-weight: 400; }
  .body-copy {
    position: absolute; left: 46px; top: 273px; width: 568px;
    font-size: 10.6px; line-height: 12.1px; letter-spacing: 0.12px;
    text-align: justify; hyphens: auto;
  }
  .body-copy p + p { margin-top: 12px; }
  .signoff { position: absolute; right: 54px; top: 752px; font-size: 16px; }
  .signature { position: absolute; left: 413px; top: 783px; width: 193px; height: 40px;
    background: linear-gradient(90deg, #e2e2e2, #d4d4d4); border-radius: 4px; }
  .footer-rule { position: absolute; left: 0; right: 0; bottom: 0; }
  .footer-rule .accent { height: 4px; background: var(--red); }
  .footer-rule .base { height: 8px; background: var(--navy); }
</style>
</head>
<body>
<main class="letterhead">
  <header>
    <div class="brand">
      <span class="brand-mark"></span>
      <span class="brand-name">Vantrell Law</span>
    </div>
    <address class="contact">
      4817 Larkspur Boulevard,<br>Suite 250,<br>Houston, Texas 77342
      <div class="contact-rule"></div>
      Phone : 832-619-3057<br>Fax : 832-407-1694
    </address>
  </header>

  <h1 class="salutation">Lorem ipsum</h1>

  <section class="body-copy">
    <p>molestie ipsum lorem nec eros. Proin vitae sodales justo. Aenean ultricies dolor vel ante faucibus facilisis. Suspendisse potenti. Duis in enim tempus odio rhoncus efficitur quis quis odio. Vestibulum eget varius nunc. Cras vitae arcu non lorem sagittis lacinia. Aenean massa dui, auctor et metus consequat, rutrum molestie augue. Curabitur tincidunt non leo sit amet commodo. Sed tempor blandit semper. Donec semper euismod sagittis. Suspendisse id neque ac nisl pharetra faucibus.</p>
    <p>Pellentesque scelerisque ipsum ac porta viverra. Aliquam facilisis fermentum orci, a vestibulum lorem dapibus nec. Proin lacinia tempus quam, in dictum turpis rhoncus eget. Vivamus nisl velit, facilisis vel tellus ut, rutrum ornare eros. Fusce at erat at erat faucibus ullamcorper. Etiam vulputate consequat pellentesque. Suspendisse a ullamcorper enim, id maximus enim. Phasellus rutrum quis libero id sodales. Praesent et pellentesque erat. Morbi in dignissim sem, eu feugiat arcu. Etiam consequat tempor sapien in cursus. Donec ultrices mollis leo ac finibus. Phasellus sollicitudin convallis tempus. Donec et quam nisi. Vivamus leo ligula, molestie non placerat ac, rutrum quis purus.</p>
    <p>Nulla suscipit enim nibh, blandit finibus dui ornare a. Nullam a porttitor libero. Nunc faucibus risus nibh, ac lobortis urna rutrum ut. Etiam viverra neque sit amet lectus posuere mollis at sit amet mi. Quisque laoreet enim sit amet neque lobortis aliquam. Cras efficitur ligula purus, vel convallis urna ecicitur vel. Etiam ligula eros, viverra sed semper ac, malesuada ac orci.</p>
    <p>Ut tincidunt placerat ipsum eget feugiat. Aenean eleifend ultricies lorem, in tempor nisi rhoncus eu. Ut cursus, turpis sit amet maximus fermentum, turpis ipsum maximus quam, vel tincidunt lectus lacus at velit. Donec nec vestibulum mauris, maximus molestie ante. Fusce suscipit volutpat molestie. Quisque in semper turpis, ornare sagittis dolor. Vestibulum pellentesque cursus cursus. In hac habitasse platea dictumst. Sed rhoncus tellus lacus, sit amet sollicitudin sem molestie blandit. Sed bibendum dictum nisl nec sollicitudin. Maecenas sit amet leo eu risus bibendum vestibulum quis vitae elit. Praesent sit amet nisl imperdiet, pulvinar mauris at, egestas tellus.</p>
    <p>Quisque gravida ullamcorper nunc ut lacinia. Donec iaculis scelerisque risus ac hendrerit. Nullam sit amet ex consectetur tortor posuere condimentum. Vestibulum a molestie sem. Quisque feugiat eget mi id cursus. Maecenas eget neque non nisi blandit pellentesque ut at nibh. Nullam nisi dolor, convallis ut hendrerit et, ornare luctus augue. Donec scelerisque, dui non venenatis volutpat, velit neque molestie nisl, quis dapibus lorem massa id velit. Cras imperdiet finibus nibh dapibus aliquet. Curabitur iaculis porttitor sem, ac euismod quam feugiat vitae. Integer fermentum orci id tellus tempor tincidunt. Praesent porta condimentum mollis. Pellentesque habitant morbi tristique senectus et netus et malesuada fames ac turpis egestas. Etiam non tristique velit, non dapibus metus. Fusce viverra facilisis augue id pretium. Cras ut convallis nisl.</p>
  </section>

  <p class="signoff">Signature</p>
  <div class="signature" role="img" aria-label="Handwritten signature"></div>

  <footer class="footer-rule" aria-hidden="true">
    <div class="accent"></div>
    <div class="base"></div>
  </footer>
</main>
</body>
</html>
```